Stationery/Logo design for law office

Hello, I am looking for a logo and stationery design for my law office. I am a solo practitioner in New York. I would like the logo to be based around my initials: KWR. Original, I know!
Hello:

I need (1) the logo, (2) a letterhead/stationery design, and (3) an envelope design. I would like the logo to be BLUE. Other than that, I am open and looking forward to seeing different designs.

For my privacy, I am using a sample name/information (the real info will be provided to the winning designer). I would like the logo to consist of the KWR design and the words "Marcus W. Reyland Law Office." I plan to use a version with both of those elements, as well as just the KWR design alone.

The information that should go in the letterhead and envelope design is the following:

Marcus W. Reyland Law Office
742 Fenwick Avenue
Suite 500
New York, New York 10003
646-382-7714
www.reylandlegal.example

I am open to different formats (changing the order of my contact info, writing the phone number without dashes, etc.); I know it's not a ton of content but I would like it to look good -- and I'm open to both classic and more modern looks.

Note that the sample colors I selected are not meant to be exclusive -- there aren't a ton of options.

Thanks in advance!

• I am leaning toward a design just based on my initials, but I am open to ideas -- just nothing trite like scales of justice or a gavel.

```html
<!DOCTYPE html>
<html lang="en">
<head>
<meta charset="utf-8">
<title>Marcus W. Reyland Law Office — Stationery</title>
<link rel="stylesheet" href="https://fonts.googleapis.com/css2?family=Orbitron:wght@700&family=Questrial&family=Tinos&display=swap">
<style>
  :root {
    --brand-blue: #0077c2;
    --paper: #ffffff;
    --ink: #1a1a1a;
    --bg-light: #f1f1f1;
    --bg-dark: #cfcfcf;
    --sheet-shadow: 0 2px 6px rgba(0,0,0,0.22);
  }
  * { box-sizing: border-box; margin: 0; padding: 0; }
  html, body { width: 1200px; height: 927px; overflow: hidden; }
  body {
    position: relative;
    background: radial-gradient(ellipse at 50% 45%, var(--bg-light) 0%, #e3e3e3 55%, var(--bg-dark) 100%);
    font-family: "Questrial", sans-serif;
  }
  .piece { position: absolute; box-shadow: var(--sheet-shadow); overflow: hidden; }
  .piece svg { position: absolute; left: 0; top: 0; }

  .wordmark { position: absolute; color: var(--brand-blue); font-family: "Orbitron", sans-serif; font-weight: 700; text-align: center; line-height: 1; white-space: nowrap; }
  .wordmark .initials { display: block; letter-spacing: 0.45em; text-indent: 0.45em; }
  .wordmark.align-left .initials { text-indent: 0; }
  .wordmark .firm { display: block; letter-spacing: 0.02em; }
  .wordmark.on-blue { color: var(--paper); }

  /* standalone logo */
  .logo-main { left: 30px; top: 384px; width: 260px; }
  .logo-main .initials { font-size: 34px; }
  .logo-main .firm { font-size: 10.6px; margin-top: 11px; }

  /* letterhead */
  .letterhead { left: 323px; top: 70px; width: 389px; height: 536px; background: var(--paper); }
  .letterhead .wordmark { left: 48px; top: 28px; text-align: left; }
  .letterhead .initials { font-size: 14px; }
  .letterhead .firm { font-size: 5px; margin-top: 4px; }
  .letter-body { position: absolute; left: 52px; top: 86px; width: 292px; font-family: "Tinos", serif; font-size: 9.3px; line-height: 12px; color: var(--ink); }
  .letter-body .recipient { margin-bottom: 36px; }
  .letter-body .salutation { margin-bottom: 23px; }
  .letter-body p { margin-bottom: 11px; }
  .letter-body .closing { margin-top: 16px; }
  .signature { position: absolute; left: 65px; top: 436px; width: 118px; height: 32px; background: linear-gradient(90deg, rgba(26,26,26,0.12), rgba(26,26,26,0.04)); border-radius: 3px; }
  .letter-footer { position: absolute; left: 40px; top: 512px; width: 310px; display: flex; justify-content: space-between; font-size: 5.8px; color: var(--ink); }

  /* folder / back sheet */
  .back-sheet { left: 756px; top: 70px; width: 388px; height: 536px; background: var(--brand-blue); }
  .back-sheet .wordmark { left: 207px; width: 170px; top: 466px; }
  .back-sheet .initials { font-size: 21px; }
  .back-sheet .firm { font-size: 6.6px; margin-top: 7px; }

  /* business cards */
  .card-front { left: 52px; top: 637px; width: 172px; height: 101px; background: var(--brand-blue); }
  .card-front .wordmark { left: 0; width: 172px; top: 36px; }
  .card-front .initials { font-size: 14px; }
  .card-front .firm { font-size: 4px; margin-top: 4px; }

  .card-back { left: 52px; top: 754px; width: 172px; height: 101px; background: var(--paper); }
  .card-back .wordmark { left: 9px; top: 7px; text-align: left; }
  .card-back .initials { font-size: 9px; }
  .card-back .firm { font-size: 3px; margin-top: 3px; }
  .card-details { position: absolute; right: 10px; top: 34px; text-align: right; color: var(--paper); font-size: 4.4px; line-height: 5.6px; }
  .card-details .name { font-size: 7.4px; font-weight: bold; margin-bottom: 4px; }
  .card-details .phone { font-size: 5.8px; font-weight: bold; margin: 6px 0 7px; }

  /* envelope */
  .envelope-front { left: 254px; top: 645px; width: 430px; height: 201px; background: var(--paper); }
  .envelope-front .wordmark { left: 19px; top: 21px; text-align: left; }
  .envelope-front .initials { font-size: 13px; }
  .envelope-front .firm { font-size: 3.9px; margin-top: 4px; }
  .envelope-address { position: absolute; left: 334px; top: 139px; color: var(--paper); font-size: 7.4px; line-height: 9px; }
  .envelope-address .web { margin-top: 16px; }

  .envelope-back { left: 714px; top: 645px; width: 430px; height: 201px; background: var(--paper); }
</style>
</head>
<body>

  <div class="wordmark logo-main">
    <span class="initials">KWR</span>
    <span class="firm">MARCUS W. REYLAND LAW OFFICE</span>
  </div>

  <section class="piece letterhead">
    <div class="wordmark align-left">
      <span class="initials">KWR</span>
      <span class="firm">MARCUS W. REYLAND LAW OFFICE</span>
    </div>
    <div class="letter-body">
      <div class="recipient">December 20, 2015<br>88 Linden Row<br>Hartwell, IN 46201</div>
      <div class="salutation">Dear Ms. Alder,</div>
      <p>Ga. Ut laccull uptium qui dolupta ssequo inctem volut latem quibusci cones molore nus doluptatur Hentotas molumquia volorrorum, atem harchil magni in perehen istrum que porum ea dentem acerio eum eatibus recupit perum rehenda.</p>
      <p>Uriam assi optibus ad qui doloria consequi dolecae sequist ma del et rent omnihitium atenis estemque nim quia eos nis cus qui re pressum, te re min et ipitasperro te quosam duntore audam qui vene desed que pereped issit, quundigni.</p>
      <p>Itamusa erchiliquis voluptamus, tes et est, que est et voluptaquae peruptius adissi odictat harchitaque solori bla del molorepudae comnimint.</p>
      <p>Equae porupis voluptat qui odit et rest facestibusam lamenisit et occumqui ut odit arum ipicipsus quam reium non et mod que velistibus eum ra videl ime velluptis quo ommolor sa as eatiberrum re con re suntios aborerferum alitasim et quibus et optas se volut el id que natur.</p>
      <div class="closing">Yours truly,</div>
    </div>
    <div class="signature" role="img" aria-label="Handwritten signature of the attorney"></div>
    <div class="letter-footer">
      <span>742 Fenwick Avenue Suite 500 New York, New York</span>
      <span>10003 646-382-7714</span>
      <span>www.reylandlegal.example</span>
    </div>
  </section>

  <section class="piece back-sheet">
    <div class="wordmark on-blue">
      <span class="initials">KWR</span>
      <span class="firm">MARCUS W. REYLAND LAW OFFICE</span>
    </div>
  </section>

  <section class="piece card-front">
    <div class="wordmark on-blue">
      <span class="initials">KWR</span>
      <span class="firm">MARCUS W. REYLAND LAW OFFICE</span>
    </div>
  </section>

  <section class="piece card-back">
    <svg width="172" height="101" viewBox="0 0 172 101" aria-hidden="true">
      <polyline points="0,66 62,66 98,16 172,16" fill="none" stroke="var(--brand-blue)" stroke-width="3"/>
      <polygon points="0,72 66,72 102,22 172,22 172,101 0,101" fill="var(--brand-blue)"/>
    </svg>
    <div class="wordmark align-left">
      <span class="initials">KWR</span>
      <span class="firm">MARCUS W. REYLAND LAW OFFICE</span>
    </div>
    <div class="card-details">
      <div class="name">Marcus W. Reyland</div>
      <div>742 Fenwick Avenue</div>
      <div>Suite 500 New York,</div>
      <div>New York 10003</div>
      <div class="phone">646-382-7714</div>
      <div>www.reylandlegal.example</div>
    </div>
  </section>

  <section class="piece envelope-front">
    <svg width="430" height="201" viewBox="0 0 430 201" aria-hidden="true">
      <polyline points="0,134 114,134 146,81 430,81" fill="none" stroke="var(--brand-blue)" stroke-width="6"/>
      <polygon points="0,141 120,141 152,89 430,89 430,201 0,201" fill="var(--brand-blue)"/>
    </svg>
    <div class="wordmark align-left">
      <span class="initials">KWR</span>
      <span class="firm">MARCUS W. REYLAND LAW OFFICE</span>
    </div>
    <div class="envelope-address">
      <div>742 Fenwick Avenue</div>
      <div>Suite 500 New York,</div>
      <div>New York 10003</div>
      <div class="web">www.reylandlegal.example</div>
    </div>
  </section>

  <section class="piece envelope-back">
    <svg width="430" height="201" viewBox="0 0 430 201" aria-hidden="true">
      <polygon points="0,0 430,0 391,58 39,58" fill="var(--brand-blue)"/>
    </svg>
  </section>

</body>
</html>
```